Coffee Roastery Label Sticker Design

We are starting a small Micro-Coffee-Roastery and are looking for a catchy design, which might look a bit hipster style, but not too much. It's called "lantern roastery", because we started roasting first in our backyard / garden by our house.
At the end of the logo and the details of the sticker (like all text elements) we need to be able to modify later by ourselfs. Coffee type, origin of coffee and so one ...
The label will be sticked on a white craftpaper coffee bag of 250grams. Sticker size around 8x12.5 cm.
The coffee bag should be an eye-catcher in a shop-shelve compared to the other coffee brands.
Another example that i really like (just to get you another idea of what we would love to get because we really like that style): https://pixvaultcdn.net/art_img/5172839/80412/61937204/qhrmzvle7k4b9x2d6wf1ny3u8p_image.png).
OR https://packfolioweb.net/blog/2016/3/14/ember-beans?

Target Market(s)

"0Speciality Coffee" lovers
High quality specialty coffee and a clear origin of the bean and fair trade or project coffee is what makes our roasted coffee product special

Logo Text

Laterne Rösterei

Requirements
Must have
• A house and a garden with either flowers or a tree is what we have in mind.
The printed label will be square 8x12.5 cm. We will use the logo on the printed label (we will print on our own printer) and on a homepage.
Nice to have
• In the attached logo example, there is no connection to a coffee business. Actually it would be a nice detail to include somehow either a descent coffee bean, a cup or a tiny roastery machine or whatever is in your mind with coffee ... (not a grinder)
Black and white is OK, but we also like colourfull very much
Please see the attached documents with sample designs that we created on our own with canvas. It's not too bad, but also a bit boring. If you have a completely different idea, please go for it. we are very open for other cool and hip designs or also quite descent and femail touch is fine too, but no must.

```html
<!DOCTYPE html>
<html lang="de">
<head>
<meta charset="utf-8">
<title>Laterne Rösterei – Filter Kaffee Etikett</title>
<link rel="stylesheet" href="https://fonts.googleapis.com/css2?family=Montserrat:wght@500;600;700&family=Arimo:wght@400&display=swap">
<style>
  :root {
    --page-bg: #ffffff;
    --label-bg: #0f1117;
    --panel: #3a4656;
    --braid: #35404f;
    --text-light: #f3f3f3;
    --text-soft: #dfe3e8;
    --mark-tone: #8a6448;
  }
  * { margin: 0; padding: 0; box-sizing: border-box; }
  html, body {
    width: 1200px; height: 900px; overflow: hidden;
    background: var(--page-bg);
  }
  .canvas {
    position: relative; width: 1200px; height: 900px;
    display: flex; align-items: center; justify-content: center;
  }
  .label {
    position: relative; width: 500px; height: 820px;
    background: var(--label-bg);
    font-family: "Montserrat", sans-serif;
    color: var(--text-light);
  }
  .braid {
    position: absolute; top: 0; bottom: 0; width: 32px;
    background: linear-gradient(180deg, var(--braid), #2c3542 50%, var(--braid));
  }
  .braid--left { left: 7px; }
  .braid--right { right: 7px; }
  .tagline {
    position: absolute; left: 79px; top: 0; width: 367px; height: 59px;
    background: var(--panel);
    display: flex; align-items: center; justify-content: center;
    font-weight: 500; font-size: 18px; letter-spacing: 4px;
    color: var(--text-soft);
  }
  .brand-name {
    position: absolute; left: 0; right: 0; text-align: center;
    font-weight: 700; font-size: 44px; letter-spacing: 12px;
    color: var(--text-light);
  }
  .brand-name--top { top: 140px; }
  .brand-name--bottom { top: 478px; }
  .brand-dot {
    position: absolute; left: 160px; top: 240px;
    width: 180px; height: 180px; border-radius: 50%;
    background: var(--mark-tone);
  }
  .product {
    position: absolute; left: 0; right: 0; top: 600px; text-align: center;
  }
  .product__type {
    font-weight: 700; font-size: 26px; letter-spacing: 3px;
  }
  .product__origin {
    margin-top: 4px;
    font-weight: 500; font-size: 20px; letter-spacing: 4px;
    color: var(--text-soft);
  }
  .details {
    position: absolute; left: 79px; top: 736px; width: 367px; height: 66px;
    background: var(--panel);
    display: flex; justify-content: space-between; align-items: center;
    padding: 0 10px 0 12px;
    font-family: "Arimo", sans-serif;
    color: var(--text-light);
  }
  .details__weight { font-size: 15px; line-height: 1.15; }
  .details__facts {
    text-align: right; font-size: 9.2px; line-height: 1.3;
    letter-spacing: 0.6px; text-transform: uppercase;
  }
  .details__facts .web { text-transform: none; }
</style>
</head>
<body>
<main class="canvas">
  <section class="label">
    <div class="braid braid--left" role="img" aria-label="Geflochtenes Ährenmuster als Randband"></div>
    <div class="braid braid--right" role="img" aria-label="Geflochtenes Ährenmuster als Randband"></div>

    <div class="tagline">SPECIALITY COFFEE</div>

    <div class="brand-name brand-name--top">LATERNE</div>
    <div class="brand-dot"></div>
    <div class="brand-name brand-name--bottom">RÖSTEREI</div>

    <div class="product">
      <p class="product__type">FILTER KAFFEE</p>
      <p class="product__origin">ÄTHIOPIEN - GUJI</p>
    </div>

    <div class="details">
      <p class="details__weight">Net Weight:<br>250 gramm</p>
      <p class="details__facts">
        Helle Röstung<br>
        Kaffee aus Äthiopien<br>
        100% Arabica / Washed<br>
        Geröstet in 6345 Lindenhof<br>
        <span class="web">www.laterne-roesterei.ch</span>
      </p>
    </div>
  </section>
</main>
</body>
</html>
```